Banner for back of trucks

We make a product that is called "Markly".
It attaches to the side of hay balers and automatically applies tags to bales as they are being made.
We require a simple / modern banner design that will be affixed to the back of hay trucks showing that the hay on board has been Marked by Markly.
The banner will be 52x91cm (landscape)
The banner needs to say "Marked by Markly" using the company logo.
It also needs the website "www.markly.com.au" displayed.
We have attached an image of our logo, the product itself and the back of a truck it will be attached to for reference.

```html
<!DOCTYPE html>
<html lang="en">
<head>
<meta charset="utf-8">
<title>Marked by Markly – Truck Banner</title>
<link rel="stylesheet" href="https://fonts.googleapis.com/css2?family=Jost:ital,wght@0,400;0,500;1,400&display=swap">
<style>
  :root {
    --bark: #564a3c;
    --mist: #d8dfd9;
    --amber: #f9ad40;
    --white: #ffffff;
  }
  html, body {
    margin: 0;
    padding: 0;
    width: 1200px;
    height: 686px;
    overflow: hidden;
    background: var(--bark);
  }
  .banner {
    display: block;
    width: 1200px;
    height: 686px;
    font-family: "Jost", "Futura", sans-serif;
  }
  .frame-warm { stroke: var(--amber); }
  .frame-cool { stroke: var(--white); }
  .headline {
    font-style: italic;
    font-weight: 400;
    font-size: 216px;
    letter-spacing: 4px;
    fill: var(--mist);
  }
  .byline {
    font-style: italic;
    font-weight: 400;
    font-size: 100px;
    letter-spacing: 24px;
  }
  .byline-by { fill: var(--mist); }
  .byline-name { fill: var(--amber); }
  .brand-name {
    font-weight: 500;
    font-size: 80px;
    fill: var(--mist);
  }
  .website {
    font-style: italic;
    font-weight: 400;
    font-size: 30px;
    letter-spacing: 6px;
    fill: var(--amber);
  }
</style>
</head>
<body>
<svg class="banner" viewBox="0 0 1200 686" xmlns="http://www.w3.org/2000/svg" aria-label="Marked by Markly banner">
  <rect width="1200" height="686" fill="var(--bark)"/>

  <g class="frame" fill="none" stroke-width="5">
    <polyline class="frame-warm" points="631,66 84,66 84,624 631,624"/>
    <polyline class="frame-cool" points="631,66 1116,66 1116,624 631,624"/>
  </g>

  <text class="headline" x="600" y="276" text-anchor="middle">MARKED</text>

  <text class="byline" x="612" y="392" text-anchor="middle"><tspan class="byline-by">BY </tspan><tspan class="byline-name">MARKLY</tspan></text>

  <rect class="rule-left" x="168" y="487" width="254" height="4" fill="var(--white)"/>
  <rect class="rule-right" x="776" y="487" width="255" height="4" fill="var(--amber)"/>

  <text class="brand-name" x="599" y="515" text-anchor="middle">Markly</text>

  <text class="website" x="602" y="585" text-anchor="middle">www.markly.com.au</text>
</svg>
</body>
</html>
```